Consulting company needs Business Cards - rough concept provided

I'm looking for someone to take our business card idea and make is slick and polished - to communicate our high-end, sophisticated, serious consulting business. We have a rough layout we did in-house. We are open to ideas on repo-ing elements, adjusting sizes, typefaces etc... within the general concept we've already come up with. We want it to be super-clean and sophisticated. We want to keep the white backgrounds, and blue brand colors. Our goal is to print with painted blue edges on thick cardstock. Thank you!!

```html
<!DOCTYPE html>
<html lang="en">
<head>
<meta charset="utf-8">
<title>Tallcrest Business Card</title>
<link rel="stylesheet" href="https://fonts.googleapis.com/css2?family=Montserrat:wght@300;400;500&family=Open+Sans:wght@300;400;700&display=swap">
<style>
  :root {
    --brand-blue: #1ea9e6;
    --brand-blue-deep: #1592d4;
    --edge-blue: #0f6fd0;
    --paper: #f8f8f8;
    --ink-grey: #6b6b6b;
    --stage: #bdbdbd;
    --white: #ffffff;
  }
  * { box-sizing: border-box; margin: 0; padding: 0; }
  html, body { width: 1200px; height: 800px; overflow: hidden; }
  body {
    background: var(--stage);
    display: flex;
    align-items: center;
    justify-content: center;
    gap: 40px;
  }
  .card {
    width: 540px;
    height: 309px;
    position: relative;
    border: 3px solid var(--edge-blue);
    overflow: hidden;
  }
  .card--front { background: var(--paper); }
  .card--back {
    background: linear-gradient(135deg, var(--brand-blue) 0%, var(--brand-blue-deep) 100%);
    color: var(--white);
  }

  /* front */
  .contact {
    position: absolute;
    left: 38px;
    top: 34px;
    font-family: "Montserrat", sans-serif;
    color: var(--ink-grey);
    font-size: 12.5px;
    line-height: 1.45;
  }
  .contact__name {
    color: var(--brand-blue);
    font-weight: 500;
    font-size: 16px;
    letter-spacing: 0.02em;
    text-transform: uppercase;
  }
  .contact__title { font-size: 14px; font-weight: 400; margin-bottom: 14px; }
  .contact__line { display: flex; align-items: center; gap: 7px; }
  .contact__line svg { width: 12px; height: 12px; fill: var(--brand-blue); flex: none; }

  .wordmark {
    font-family: "Open Sans", sans-serif;
    font-weight: 700;
    letter-spacing: 0.01em;
    line-height: 1;
  }
  .card--front .wordmark {
    position: absolute;
    left: 34px;
    bottom: 30px;
    font-size: 62px;
    color: var(--brand-blue);
  }

  /* back */
  .statement {
    position: absolute;
    left: 38px;
    top: 34px;
    right: 30px;
    font-family: "Open Sans", sans-serif;
    font-weight: 300;
    font-size: 18px;
    line-height: 1.3;
  }
  .statement strong { font-weight: 700; }
  .card--back .wordmark {
    position: absolute;
    left: 34px;
    bottom: 30px;
    font-size: 62px;
    color: var(--white);
  }
</style>
</head>
<body>
  <section class="card card--front" aria-label="Business card front">
    <div class="contact">
      <p class="contact__name">Dana Whitlow</p>
      <p class="contact__title">Brand Consultant</p>
      <p class="contact__line">4820 Harbor Lane,</p>
      <p class="contact__line">Ste 210 Fairview, CA 90311</p>
      <p class="contact__line">
        <svg viewBox="0 0 24 24" aria-hidden="true"><path d="M6.6 10.8a15.1 15.1 0 0 0 6.6 6.6l2.2-2.2a1 1 0 0 1 1-.25 11.4 11.4 0 0 0 3.6.57 1 1 0 0 1 1 1V20a1 1 0 0 1-1 1A17 17 0 0 1 3 4a1 1 0 0 1 1-1h3.5a1 1 0 0 1 1 1c0 1.25.2 2.45.57 3.57a1 1 0 0 1-.25 1z"/></svg>
        (555) 310 4172
      </p>
      <p class="contact__line">
        <svg viewBox="0 0 24 24" aria-hidden="true"><path d="M2 5h20v14H2z M2 5l10 8 10-8" fill="none" stroke="#1ea9e6" stroke-width="2.4"/></svg>
        dana@tallcrest.com
      </p>
    </div>
    <p class="wordmark">TALLCREST</p>
  </section>

  <section class="card card--back" aria-label="Business card back">
    <p class="statement">
      <strong>We help</strong> [target demographic] <strong>achieve</strong>
      [desired emotional outcome] <strong>by</strong>
      [our unique approach] <strong>because</strong>
      [our brand beliefs]
    </p>
    <p class="wordmark">TALLCREST</p>
  </section>
</body>
</html>
```